Health & Beauty Company- Business Card Design

Two-sided business card design and logo design.

Company markets and sells otc treatments for the health and beauty industry. Marketing products to doctors, pharmacists and retail drug companies like dorvellas, pmn and velo mart.

Designs should be submitted as vector based PDFs. To keep your text in vector format, our printer recommends applications like Adobe Illustrator, Adobe InDesign and more recent versions of Adobe Photoshop.

Target Market(s)

Drug stores, doctors and pharmacists

Industry/Entity Type

Printer

Requirements
Must have
• Back side of business card should include company logo and our tagline: "Elevating Everyday Wellness & Care"

Company name acronym must be included: NRTK

```html
<!DOCTYPE html>
<html lang="en">
<head>
<meta charset="utf-8">
<title>NRTK Business Card</title>
<link href="https://fonts.googleapis.com/css2?family=Jost:wght@400;500&display=swap" rel="stylesheet">
<style>
  :root {
    --backdrop: #8d8d8b;
    --card: #0b0b0b;
    --card-edge: #1a1a1a;
    --ink: #f2f2f2;
    --ink-soft: #d6d6d6;
    --gloss: #262626;
    --gloss-light: #3a3a3a;
    --tagline: #444444;
  }
  * { margin: 0; padding: 0; box-sizing: border-box; }
  html, body { width: 1200px; height: 774px; overflow: hidden; }
  body {
    background: var(--backdrop);
    font-family: "Jost", "Futura", sans-serif;
    color: var(--ink);
    position: relative;
  }
  .card {
    position: absolute;
    top: 232px;
    width: 540px;
    height: 309px;
    background: var(--card);
    border: 1px solid var(--card-edge);
    box-shadow: 0 12px 30px rgba(0,0,0,0.35);
  }
  .card--front { left: 40px; }
  .card--back { left: 620px; }

  /* Front */
  .brand {
    position: absolute;
    left: 40px;
    top: 66px;
    width: 140px;
    display: flex;
    flex-direction: column;
    align-items: center;
    gap: 18px;
  }
  .brand__dot {
    width: 70px; height: 70px;
    border-radius: 50%;
    background: var(--ink-soft);
  }
  .brand__name {
    font-size: 38px;
    font-weight: 500;
    letter-spacing: 3px;
    line-height: 1;
    color: var(--ink);
  }
  .person {
    position: absolute;
    left: 218px;
    top: 40px;
    width: 260px;
  }
  .person__name {
    font-size: 24px;
    font-weight: 400;
    letter-spacing: 1.5px;
    line-height: 1.2;
    padding-bottom: 3px;
    border-bottom: 1px solid var(--ink-soft);
  }
  .person__title {
    font-size: 11px;
    margin-top: 6px;
    color: var(--ink-soft);
  }
  .contact {
    position: absolute;
    left: 222px;
    top: 150px;
    font-size: 12px;
    line-height: 17px;
    color: var(--ink-soft);
    display: grid;
    grid-template-columns: 56px auto;
    column-gap: 4px;
  }
  .contact__gap { grid-column: 1 / 3; height: 8px; }

  /* Back */
  .emblem {
    position: absolute;
    left: 50%;
    top: 40px;
    transform: translateX(-50%);
    width: 176px; height: 176px;
    border-radius: 50%;
    background: radial-gradient(circle at 40% 35%, var(--gloss-light), var(--gloss));
    display: flex;
    align-items: center;
    justify-content: center;
  }
  .emblem__name {
    font-size: 46px;
    font-weight: 500;
    letter-spacing: 4px;
    line-height: 1;
    color: var(--card);
  }
  .tagline {
    position: absolute;
    left: 0; right: 0;
    bottom: 48px;
    text-align: center;
    font-size: 14px;
    letter-spacing: 2.5px;
    text-transform: uppercase;
    color: var(--tagline);
  }
</style>
</head>
<body>
  <section class="card card--front">
    <div class="brand">
      <span class="brand__dot"></span>
      <span class="brand__name">NRTK</span>
    </div>
    <div class="person">
      <h1 class="person__name">NAME SURNAME</h1>
      <p class="person__title">President &amp; CEO</p>
    </div>
    <div class="contact">
      <span>Address</span><span>: Your Address Goes Here</span>
      <span></span><span>&nbsp;&nbsp;City, State, Zipcode</span>
      <span class="contact__gap"></span>
      <span>Phone</span><span>: xxx.xxx.xxxx</span>
      <span>Fax</span><span>: xxx.xxx.xxxx</span>
      <span>E-mail</span><span>: xxxx@xxxxxxxxxxxxxxx.com</span>
      <span>Skype</span><span>: xxxxxx.xxxxx</span>
    </div>
  </section>

  <section class="card card--back">
    <div class="emblem">
      <span class="emblem__name">NRTK</span>
    </div>
    <p class="tagline">Elevating Everyday Wellness &amp; Care</p>
  </section>
</body>
</html>
```